VORELT/M&H - brochure vol III

We have 2 property companies;
VORELT – Development Consultants - http://vorelt.co.uk/
Marsh & Harbour Commercial – Commercial Property Agents - http://marshandharbour.com/
We have 2 VORELT brochures and 1 Marsh & Harbour brochure, with almost the same content.
We need someone to design a 3rd brochure. The content will be a combination of the content of in our previous brochures. We can provide all images and text. Once the brochure is designed, we will need 2 versions – almost identical content but 2 different front covers (one for each company).
We have many reference examples of brochure designs that we love.
Any questions please let me know!
Thank you,
Wendy

```html
<!DOCTYPE html>
<html lang="en">
<head>
<meta charset="utf-8">
<title>VORELT – Brochure Volume III</title>
<link href="https://fonts.googleapis.com/css2?family=Montserrat:wght@400;500;600;700&display=swap" rel="stylesheet">
<style>
:root{
  --stage:#2c2c2c;
  --paper:#f7f7f7;
  --paper-edge:#ececec;
  --gold:#f7ac2a;
  --ink:#2b2b2b;
  --muted:#555;
  --label:#bdbdbd;
  --map-land:#5c5b5d;
  --map-base:#dcdcdc;
}
*{margin:0;padding:0;box-sizing:border-box}
html,body{width:861px;height:1200px;overflow:hidden;background:var(--stage);font-family:"Montserrat",sans-serif;color:var(--ink)}
.spread{position:relative;width:861px;height:1200px}
.page{position:absolute;width:363px;height:257px;background:linear-gradient(90deg,var(--paper-edge),var(--paper) 20%,#fff 50%,var(--paper) 80%,var(--paper-edge));overflow:hidden}
.page-label{position:absolute;font-size:8px;color:var(--label);transform:rotate(-90deg);transform-origin:left bottom;white-space:nowrap}
.fill{position:absolute}
.band{position:absolute;top:0;height:100%;width:14px;background:var(--gold)}
.project-title{font-size:10.5px;font-weight:700;line-height:1.1;text-transform:uppercase;color:var(--ink)}
.project-type{font-size:5.2px;font-weight:600;color:var(--gold);text-transform:uppercase;margin-top:4px}
.project-intro{font-size:4.6px;line-height:1.5;color:var(--muted);margin-top:10px}
.facts{list-style:none;margin-top:8px}
.facts li{font-size:4.6px;line-height:1;color:var(--muted);margin-bottom:5.4px}
.facts b{font-weight:700;color:var(--ink)}

/* cover */
.cover-box{position:absolute;left:104px;top:74px;width:155px;height:97px;border:1.5px solid var(--gold);outline:4px solid #fff;background:#fff;text-align:center}
.cover-name{font-size:33px;font-weight:600;color:var(--gold);margin-top:13px;letter-spacing:0.5px;line-height:1}
.cover-tag{font-size:8px;font-weight:500;color:var(--gold);line-height:1.5;margin-top:6px;letter-spacing:0.4px}
.cover-volume{position:absolute;left:0;width:100%;top:177px;text-align:center;font-size:10px;font-weight:600;color:var(--gold)}

/* focus */
.focus-heading{position:absolute;left:12px;top:122px;font-size:14px;font-weight:700;color:var(--gold);transform:rotate(-90deg);transform-origin:left top;white-space:nowrap;letter-spacing:0.3px}

/* about */
.about-box{position:absolute;left:192px;top:66px;width:154px;height:118px;border:1px solid var(--gold);border-left:none;padding:6px 8px 0 11px}
.about-title{font-size:15px;font-weight:700;color:var(--gold);line-height:1}
.about-text{font-size:4.3px;line-height:1.55;color:var(--muted);text-align:justify;margin-top:6px}
.about-text+.about-text{margin-top:4px}

.detail-box{position:absolute;border:1px solid var(--gold);border-left:none;border-right:none;padding:12px 10px 0 11px;background:#fff}
</style>
</head>
<body>
<div class="spread">

  <!-- Page 1: cover -->
  <section class="page" style="left:46px;top:40px">
    <div class="cover-box">
      <div class="cover-name">VORELT</div>
      <div class="cover-tag">LONDON'S DEVELOPMENT<br>CONSULTANT</div>
    </div>
    <div class="cover-volume">VOLUME III</div>
  </section>
  <div class="page-label" style="left:430px;top:285px">Page 1</div>

  <!-- Page 2: focus areas -->
  <section class="page" style="left:455px;top:40px">
    <h2 class="focus-heading">FOCUS AREAS</h2>
    <div class="fill" role="img" aria-label="Map of London and the south east with the focus boroughs shaded dark grey and the Thames in gold" style="left:32px;top:14px;width:315px;height:227px;background:linear-gradient(180deg,var(--map-base) 0%,var(--map-base) 35%,var(--map-land) 40%,var(--map-land) 100%)"></div>
  </section>
  <div class="page-label" style="left:839px;top:285px">Page 2</div>

  <!-- Page 3: about us -->
  <section class="page" style="left:46px;top:325px">
    <div class="fill" role="img" aria-label="Dark map of central and south east London boroughs with the Thames in gold" style="left:15px;top:15px;width:177px;height:227px;background:linear-gradient(180deg,#c8c8c8 0%,#c8c8c8 22%,#3e3d3f 22%,#3a393b 100%)"></div>
    <div class="about-box">
      <h2 class="about-title">ABOUT US</h2>
      <p class="about-text">VORELT Property is a leading London based development consultancy specialising in the acquisition and disposal of brownfield sites with potential for residential development.</p>
      <p class="about-text">Our expertise is in identifying opportunities where developers can add value through planning permission or strategic asset management. Our considerable knowledge of the development market and creative approach to delivering maximum value, has enabled us to become one of the most active development consultancies in South East London and Kent.</p>
    </div>
  </section>
  <div class="page-label" style="left:430px;top:570px">Page 3</div>

  <!-- Page 4: Falcon Row -->
  <section class="page" style="left:455px;top:325px">
    <div class="band" style="left:0"></div>
    <div style="position:absolute;left:26px;top:14px;width:140px">
      <h3 class="project-title">54 Falcon Row,<br>London SE1</h3>
      <div class="project-type">Landmark Development</div>
      <p class="project-intro" style="margin-top:24px">Acquisition of an existing office building with the benefit of full planning permission for the development of a 16 storey mixed use scheme.</p>
      <ul class="facts">
        <li><b>Scheme</b> – 9 x Luxury apartments; 16 storeys</li>
        <li><b>Borough</b> – Southwark</li>
        <li><b>Existing use</b> – Office</li>
        <li><b>Vendor/Selling agent</b> – Brightmoor Estates</li>
        <li><b>Purchaser</b> – Private Client</li>
        <li><b>Project value</b> – £20,000,000</li>
      </ul>
    </div>
    <div class="fill" role="img" aria-label="Street view of a brick mid-rise office building on a corner" style="left:173px;top:15px;width:174px;height:226px;background:linear-gradient(180deg,#b8cde6 0%,#d7dfe6 35%,#8a5a4a 55%,#7d7470 100%)"></div>
    <div class="fill" role="img" aria-label="Street photo of the building entrance" style="left:17px;top:205px;width:38px;height:37px;background:linear-gradient(#cfd6dc,#9a8779)"></div>
    <div class="fill" role="img" aria-label="Close view of the building number" style="left:56px;top:205px;width:38px;height:37px;background:linear-gradient(#b59b82,#6f5443)"></div>
    <div class="fill" role="img" aria-label="View along the street" style="left:95px;top:205px;width:38px;height:37px;background:linear-gradient(#dfe5ea,#8c8d8f)"></div>
    <div class="fill" role="img" aria-label="Tower block seen from below" style="left:134px;top:205px;width:28px;height:37px;background:linear-gradient(#c4d4e4,#6d7c8a)"></div>
  </section>
  <div class="page-label" style="left:839px;top:570px">Page 4</div>

  <!-- Page 5: Kestrel Yard -->
  <section class="page" style="left:46px;top:614px">
    <div class="fill" role="img" aria-label="Aerial view of the site with plot boundaries outlined in red" style="left:15px;top:14px;width:333px;height:94px;background:linear-gradient(180deg,#9a9a98,#6e6f6d 60%,#8b8884)"></div>
    <div style="position:absolute;left:20px;top:118px;width:185px">
      <h3 class="project-title">3-11 Kestrel Yard,<br>London E1</h3>
      <div class="project-type">Residential Development Site</div>
      <p class="project-intro" style="margin-top:3px;text-align:justify">Identified and delivered development opportunity with planning permission for a mixed use scheme comprising 78 apartments in the City Fringe.</p>
      <ul class="facts">
        <li><b>Scheme</b> – 78 x Residential apartments</li>
        <li><b>Borough</b> – Tower Hamlets</li>
        <li><b>Existing use</b> – Car repairs centre</li>
        <li><b>Vendor/Selling agent</b> – Halvers</li>
        <li><b>Purchaser</b> – Westgrove Housing Group</li>
        <li><b>Project value</b> – £30,000,000</li>
      </ul>
    </div>
    <div class="fill" role="img" aria-label="Overhead photo of the yard with parked cars and green roof" style="left:215px;top:111px;width:133px;height:75px;background:linear-gradient(180deg,#a08a74,#6f8a5a 50%,#5b6670)"></div>
    <div class="fill" role="img" aria-label="Photo of surrounding apartment blocks and the yard" style="left:215px;top:191px;width:133px;height:51px;background:linear-gradient(180deg,#c9d5df,#9a6a5a 60%,#66696c)"></div>
  </section>
  <div class="page-label" style="left:430px;top:860px">Page 5</div>

  <!-- Page 6: Linden Street -->
  <section class="page" style="left:455px;top:614px">
    <div class="band" style="left:0"></div>
    <div class="detail-box" style="left:26px;top:48px;width:146px;height:156px">
      <h3 class="project-title">Linden Street,<br>Maidstone ME16</h3>
      <div class="project-type" style="margin-top:9px">Residential Development Site</div>
      <p class="project-intro" style="margin-top:8px">Delivered consented development site with planning permission for 22 dwellings to housing association, off market.</p>
      <ul class="facts">
        <li><b>Scheme</b> – 22 x Social housing units</li>
        <li><b>Borough</b> – Maidstone</li>
        <li><b>Existing use</b> – Business Centre</li>
        <li><b>Vendor/Selling agent</b> – Private individual</li>
        <li><b>Purchaser</b> – Larkfield Housing Association</li>
        <li><b>Project value</b> – £5,000,000</li>
      </ul>
    </div>
    <div class="fill" role="img" aria-label="Illustrated street scene of new brick terraced houses with trees" style="left:173px;top:15px;width:174px;height:143px;background:linear-gradient(180deg,#d8e4ec 0%,#b9705c 40%,#9aa886 75%,#c9c7c0)"></div>
    <div class="fill" role="img" aria-label="Site layout plan with plot outlines" style="left:173px;top:166px;width:174px;height:75px;background:linear-gradient(135deg,#f2f2f2,#e3e3e3)"></div>
  </section>
  <div class="page-label" style="left:839px;top:860px">Page 6</div>

  <!-- Page 7: Alder Road -->
  <section class="page" style="left:256px;top:902px">
    <div class="fill" role="img" aria-label="Visual of the new mixed use building on a busy street" style="left:15px;top:16px;width:177px;height:110px;background:linear-gradient(180deg,#e2e0dc 0%,#b7906c 45%,#8c7a6e 100%)"></div>
    <div class="fill" role="img" aria-label="Street level visual of the building with trees" style="left:15px;top:131px;width:177px;height:109px;background:linear-gradient(180deg,#d9dcdf 0%,#c2a584 50%,#7f7a74 100%)"></div>
    <div class="detail-box" style="left:192px;top:48px;width:155px;height:157px;border-right:1px solid var(--gold)">
      <h3 class="project-title">Alder Road,<br>London SE5</h3>
      <div class="project-type" style="margin-top:9px">Petrol Filling Station</div>
      <p class="project-intro" style="margin-top:8px">Acquisition of small petrol station portfolio from Fuelpoint including site in Camberwell with planning permission for the development of 9 apartments and a retail space to let to Greenbay Foods.</p>
      <ul class="facts">
        <li><b>Scheme</b> – 9 x Private flats</li>
        <li><b>Borough</b> – Southwark</li>
        <li><b>Existing use</b> – Petrol Station</li>
        <li><b>Vendor/Selling agent</b> - Fuelpoint</li>
        <li><b>Purchaser</b> – Private client</li>
        <li><b>Project value</b> – £7,000,000</li>
      </ul>
    </div>
    <div class="band" style="left:353px;width:10px"></div>
  </section>
  <div class="page-label" style="left:640px;top:1148px">Page 7</div>

</div>
</body>
</html>
```